Willow Crest Beauty - Package Design

New Beauty label needing product packaging design. Looking for elegant and stylish design to represent our premium brand.

This project is for 1 label and 1 box design. The winning designer will be assigned another project for the next product in the range. (to be paid as a new project)

This product is for "Glacier Pearl Mask". Please see the label format and jar attached. Please note there are 2 different jars we are considering (will have a mud inside). Please feel free to choose whichever one suits your design best.

The labels and boxes are to retain the product information, such as size, ingredients etc, but is to be updated to our brand. You can move or display the other information as you wish.

the size of the glacier pearl mask color box is 72*72*85mm (length*width*height)
the size of glacier pearl mask label is 218*58mm (width*height)

Women 15 to 65

• Must be elegant and represent our brand which is a premium beauty product.
• Dark blue. Dark purple etc. Colours should compliment the logo

```html
<!DOCTYPE html>
<html lang="en">
<head>
<meta charset="utf-8">
<title>Willow Crest Beauty – Glacier Pearl Mask Packaging</title>
<link href="https://fonts.googleapis.com/css2?family=Arimo:wght@400;700&family=Oswald:wght@600&display=swap" rel="stylesheet">
<style>
  :root{
    --paper:#ffffff;
    --board:#1c1a36;
    --board-edge:#121026;
    --fold:#b23a96;
    --glow:#e4e0f6;
    --glow-soft:#b9b2e0;
    --glow-mid:#6c64a8;
    --glow-deep:#2e2a55;
    --ink:#ffffff;
    --title:#f3dc4a;
    --gold:#d3a73c;
    --badge:#f2f1f8;
    --art:#2a2540;
  }
  html,body{margin:0;padding:0;width:1200px;height:1200px;overflow:hidden;background:var(--paper);}
  .sheet{position:relative;width:1500px;height:1500px;transform:scale(.8);transform-origin:0 0;font-family:"Arimo",Arial,sans-serif;color:var(--ink);}
  .dieline{position:absolute;left:0;top:0;}
  .glow-panel{position:absolute;overflow:hidden;}
  .glow-front{left:405px;top:616px;width:315px;height:387px;
    background:radial-gradient(ellipse 62% 55% at 58% 40%,var(--glow) 0%,var(--glow-soft) 28%,var(--glow-mid) 52%,var(--glow-deep) 78%,var(--board) 100%);}
  .glow-back{left:720px;top:616px;width:317px;height:387px;
    background:radial-gradient(ellipse 45% 40% at -5% 40%,#4e4785 0%,#2a264d 55%,var(--board) 100%);}
  .glow-lid{left:88px;top:245px;width:317px;height:371px;
    background:radial-gradient(ellipse 62% 55% at 70% 30%,var(--glow) 0%,var(--glow-soft) 28%,var(--glow-mid) 52%,var(--glow-deep) 78%,var(--board) 100%);}
  .label{position:absolute;left:513px;top:63px;width:957px;height:255px;
    background:radial-gradient(ellipse 150px 125px at 257px 100px,var(--glow) 0%,var(--glow-soft) 30%,var(--glow-mid) 58%,#17152d 100%);
    background-color:#17152d;}
  .brand{position:absolute;font-family:"Arimo",Arial,sans-serif;font-weight:400;color:var(--gold);text-align:center;letter-spacing:.06em;text-transform:uppercase;line-height:1.2;white-space:nowrap;}
  .brand small{display:block;font-size:.42em;letter-spacing:.55em;}
  .mask-art{position:absolute;border-radius:50%;background:radial-gradient(circle at 45% 40%,#4a4366 0%,var(--art) 70%);}
  .product-title{position:absolute;font-family:"Oswald","Arial Narrow",sans-serif;font-weight:600;color:var(--title);text-align:center;white-space:nowrap;text-shadow:0 1px 2px rgba(0,0,0,.5);}
  .size{position:absolute;font-weight:700;text-align:center;white-space:nowrap;}
  .flip{transform:rotate(180deg);}
  .badge{position:absolute;border-radius:50%;background:var(--badge);}
  .copy{position:absolute;text-align:justify;line-height:1.25;}
  .copy p{margin:0;}
  .copy .head{text-align:left;}
  .maker{position:absolute;line-height:1.3;}
  .code-box{position:absolute;background:#fff;}
  .icon{position:absolute;}
  .icon-label{font-weight:700;text-align:center;line-height:1.05;position:absolute;}
</style>
</head>
<body>
<div class="sheet">

  <svg class="dieline" width="1500" height="1500" viewBox="0 0 1500 1500" aria-hidden="true">
    <g fill="var(--board-edge)">
      <path d="M75,616 L75,215 Q75,170 120,170 L373,170 Q418,170 418,215 L418,616 Z"/>
      <polygon points="30,645 75,616 88,616 88,1003 75,1003 30,975"/>
      <rect x="75" y="616" width="1291" height="387"/>
      <polygon points="405,616 405,408 672,408 715,578 735,578 735,616"/>
      <rect x="735" y="604" width="287" height="14"/>
      <polygon points="1022,616 1022,578 1040,578 1082,408 1348,408 1348,595 1366,610 1366,616"/>
      <polygon points="405,1003 405,1030 418,1030 458,1200 705,1200 705,1003"/>
      <path d="M705,1003 L705,1380 Q705,1435 760,1435 L995,1435 Q1050,1435 1050,1380 L1050,1003 Z"/>
      <polygon points="1037,1003 1037,1200 1303,1200 1340,1034 1366,1034 1366,1003"/>
    </g>
    <g fill="var(--board)">
      <path d="M88,616 L88,230 Q88,183 128,183 L365,183 Q405,183 405,230 L405,616 Z"/>
      <polygon points="43,650 88,628 88,990 43,968"/>
      <rect x="88" y="616" width="1265" height="387"/>
      <polygon points="418,616 418,420 662,420 705,590 722,590 722,616"/>
      <polygon points="1035,616 1035,590 1050,590 1095,420 1335,420 1335,600 1353,612 1353,616"/>
      <polygon points="418,1003 418,1020 430,1020 470,1188 705,1188 705,1003"/>
      <path d="M718,1003 L718,1375 Q718,1422 765,1422 L990,1422 Q1037,1422 1037,1375 L1037,1003 Z"/>
      <polygon points="1050,1003 1050,1188 1292,1188 1328,1022 1353,1022 1353,1003"/>
    </g>
    <g fill="none" stroke="var(--fold)" stroke-width=".8" opacity=".8">
      <line x1="88" y1="245" x2="405" y2="245"/>
      <line x1="88" y1="616" x2="1353" y2="616"/>
      <line x1="88" y1="1003" x2="1353" y2="1003"/>
      <line x1="405" y1="245" x2="405" y2="1003"/>
      <line x1="720" y1="616" x2="720" y2="1003"/>
      <line x1="1037" y1="616" x2="1037" y2="1003"/>
      <line x1="88" y1="616" x2="88" y2="1003"/>
      <line x1="1353" y1="616" x2="1353" y2="1003"/>
      <line x1="718" y1="1365" x2="1037" y2="1365"/>
    </g>
  </svg>

  <!-- Lid panel, printed upside down -->
  <div class="glow-panel glow-lid"></div>
  <div class="size flip" style="left:88px;top:280px;width:317px;font-size:14px;">250 I 8.8fl.oz</div>
  <div class="product-title flip" style="left:88px;top:370px;width:317px;font-size:33px;">GLACIER PEARL MASK</div>
  <div class="brand flip" style="left:120px;top:462px;width:250px;font-size:25px;">Willow Crest<small>Beauty</small></div>

  <!-- Directions side -->
  <div class="copy" style="left:110px;top:657px;width:273px;font-size:14.6px;">
    <p class="head">DIRECTIONS</p>
    <p>Gently massage a thin layer of mud onto Cleansed skin in a gentle downwar motion. Leave th emud on the skin for 7-12 Minutes allowing mud to slightly dry. If the mud begins to crack and itch - it has been on too long. To remove the mask, lay a lukewarm wash cloth on your face for a few seconds to soften the mud, and then rinse remaining mud off with warm water. Do not scrub as you remove the mask.</p>
    <p class="head" style="margin-top:18px;">CAUTION<br>FOR EXTERNAL USE ONLY</p>
  </div>

  <!-- Front -->
  <div class="glow-panel glow-front"></div>
  <div class="brand" style="left:435px;top:696px;width:250px;font-size:26px;">Willow Crest<small>Beauty</small></div>
  <div class="mask-art" role="img" aria-label="Illustration of a dark clay face mask with water droplets" style="left:537px;top:777px;width:56px;height:64px;"></div>
  <div class="product-title" style="left:405px;top:840px;width:315px;font-size:32px;">GLACIER PEARL MASK</div>
  <div class="badge" style="left:646px;top:895px;width:60px;height:60px;"></div>
  <div class="size" style="left:405px;top:958px;width:290px;font-size:14px;">250 I 8.8fl.oz</div>

  <!-- Back -->
  <div class="glow-panel glow-back"></div>
  <div class="copy" style="left:742px;top:657px;width:273px;font-size:16.3px;">
    <p class="head">INGREDIENTS:</p>
    <p>Deiconized Water, Pure Dead Sea Mud, Kaolin, Shea Butter, Sunflower Oil, Aloe Vera Juice, Vegetable Glycerin, Jojoba Oil, Hickory Bark Extract, Calendula Oil, Xanthan Gum, Vitamin E, Hyaluronic Acid</p>
  </div>
  <svg class="icon" style="left:745px;top:848px;" width="50" height="56" viewBox="0 0 50 56" aria-hidden="true">
    <path d="M4,20 L40,2" stroke="#fff" stroke-width="2" fill="none"/>
    <path d="M6,28 L44,28 L40,52 L10,52 Z" stroke="#fff" stroke-width="2" fill="none"/>
    <text x="25" y="47" fill="#fff" font-family="Arimo, sans-serif" font-size="11" text-anchor="middle">12M</text>
  </svg>
  <div class="icon" role="img" aria-label="Cruelty-free rabbit symbol" style="left:824px;top:856px;width:46px;height:30px;border-radius:40% 40% 20% 20%;background:radial-gradient(circle,#a9a4c8 0%,#5e5888 80%);"></div>
  <div class="icon-label" style="left:812px;top:889px;width:70px;font-size:8px;">NOT TESTED<br>ON ANIMALS</div>
  <div class="maker" style="left:739px;top:913px;font-size:16px;">Manufactured for:<br>Halvern Bay<br>Trading Co., ltd</div>
  <div class="code-box" style="left:885px;top:877px;width:144px;height:91px;"></div>

  <!-- Jar label -->
  <div class="label"></div>
  <div class="brand" style="left:665px;top:108px;width:200px;font-size:21px;">Willow Crest<small>Beauty</small></div>
  <div class="mask-art" role="img" aria-label="Illustration of a dark clay face mask with water droplets" style="left:746px;top:163px;width:42px;height:48px;"></div>
  <div class="product-title" style="left:640px;top:210px;width:255px;font-size:24px;">GLACIER PEARL MASK</div>
  <div class="badge" style="left:553px;top:222px;width:62px;height:62px;"></div>
  <div class="size" style="left:640px;top:298px;width:232px;font-size:11px;">250 I 8.8fl.oz</div>
  <div class="copy" style="left:964px;top:73px;width:462px;font-size:11px;line-height:1.38;">
    <p class="head">DIRECTIONS</p>
    <p>Gently massage a thin layer of mud onto Cleansed skin in a gentle downwar motion. Leave th emud on the skin for 7-12 Minutes allowing mud to slightly dry. If the mud begins to crack and itch - it has been on too long. To remove the mask, lay a lukewarm wash cloth on your face for a few seconds to soften the mud, and then rinse remaining mud off with warm water. Do not scrub as you remove the mask.</p>
    <p class="head" style="margin-top:14px;">CAUTION<br>FOR EXTERNAL USE ONLY<br>Keep out of reach of children</p>
  </div>
  <svg class="icon" style="left:965px;top:242px;" width="30" height="34" viewBox="0 0 50 56" aria-hidden="true">
    <path d="M4,20 L40,2" stroke="#fff" stroke-width="2" fill="none"/>
    <path d="M6,28 L44,28 L40,52 L10,52 Z" stroke="#fff" stroke-width="2" fill="none"/>
    <text x="25" y="47" fill="#fff" font-family="Arimo, sans-serif" font-size="11" text-anchor="middle">12M</text>
  </svg>
  <div class="icon" role="img" aria-label="Cruelty-free rabbit symbol" style="left:1014px;top:248px;width:28px;height:18px;border-radius:40% 40% 20% 20%;background:radial-gradient(circle,#a9a4c8 0%,#5e5888 80%);"></div>
  <div class="icon-label" style="left:1005px;top:267px;width:46px;font-size:5px;">NOT TESTED<br>ON ANIMALS</div>
  <div class="badge" style="left:1178px;top:244px;width:43px;height:43px;"></div>
  <div class="maker" style="left:964px;top:279px;font-size:11px;">Manufactured for:<br>Halvern Bay Trading Co., ltd</div>
  <div class="code-box" style="left:1307px;top:245px;width:128px;height:64px;"></div>

</div>
</body>
</html>
```